Criação de Papelaria Profissional para Beleza
A empresa queria:
" Espaço físico tipo loja com cabines exclusivas para depilação, método Espanhol com cera quente. Única com cauterização pós depilação. E espaço dedicado a beleza das mãos e pés "

```html
<!DOCTYPE html>
<html lang="pt-BR">
<head>
<meta charset="UTF-8">
<title>Tavessa Depil e Unhas — Cartão de Visita</title>
<link href="https://fonts.googleapis.com/css2?family=Montserrat:wght@400;500;600;700&display=swap" rel="stylesheet">
<style>
  :root {
    --page-bg: #ecebe8;
    --card-light: #ffffff;
    --card-dark: #2e1f26;
    --pink: #e0488f;
    --pink-deep: #c92f78;
    --ink: #2a2a2a;
    --ink-soft: #555555;
  }
  * { margin: 0; padding: 0; box-sizing: border-box; }
  html, body {
    width: 1200px; height: 1200px; overflow: hidden;
    background: var(--page-bg);
    font-family: "Montserrat", sans-serif;
  }
  .sheet {
    width: 1200px; height: 1200px;
    display: flex; flex-direction: column; align-items: center; justify-content: center;
    gap: 60px;
  }
  .card {
    position: relative;
    width: 880px; height: 500px;
    border-radius: 30px;
    overflow: hidden;
    box-shadow: 0 10px 30px rgba(0,0,0,0.12);
  }
  .card--front { background: var(--card-light); }
  .card--back { background: var(--card-dark); }

  .card__edge {
    position: absolute; left: 0; bottom: 0;
    width: 100%; height: 30px;
  }

  /* Front side */
  .identity {
    position: absolute; left: 70px; top: 62px;
    padding-left: 22px;
    border-left: 8px solid var(--pink);
  }
  .identity__name {
    font-size: 30px; font-weight: 700; color: var(--ink);
    letter-spacing: 0.5px; line-height: 1.15;
  }
  .identity__role {
    font-size: 24px; font-weight: 400; color: var(--ink-soft);
    margin-top: 4px;
  }
  .contacts {
    position: absolute; left: 70px; top: 196px;
    list-style: none;
    display: flex; flex-direction: column; gap: 14px;
  }
  .contacts__item {
    display: flex; align-items: flex-start; gap: 14px;
    font-size: 19px; color: var(--ink); line-height: 1.2;
  }
  .contacts__icon {
    flex: 0 0 28px; width: 28px; height: 28px;
  }

  .brand {
    position: absolute;
    display: flex; flex-direction: column; align-items: center;
    color: var(--pink);
  }
  .brand__mark {
    border-radius: 50%;
    background: var(--pink);
  }
  .brand__name {
    font-weight: 600;
    color: var(--pink);
    letter-spacing: 1px;
    line-height: 1;
  }
  .brand__tagline {
    font-weight: 500;
    color: var(--pink);
    letter-spacing: 2px;
    text-transform: uppercase;
  }

  .brand--front { right: 70px; top: 170px; width: 330px; }
  .brand--front .brand__mark { width: 56px; height: 56px; margin-bottom: 16px; }
  .brand--front .brand__name { font-size: 62px; }
  .brand--front .brand__tagline { font-size: 18px; margin-top: 10px; }

  .brand--back { left: 50%; top: 50%; transform: translate(-50%, -54%); width: 480px; }
  .brand--back .brand__mark { width: 80px; height: 80px; margin-bottom: 22px; }
  .brand--back .brand__name { font-size: 90px; }
  .brand--back .brand__tagline { font-size: 24px; margin-top: 12px; }
</style>
</head>
<body>
<main class="sheet">

  <section class="card card--front" aria-label="Frente do cartão">
    <div class="identity">
      <p class="identity__name">NOME E SOBRENOME</p>
      <p class="identity__role">Cargo | Função</p>
    </div>

    <ul class="contacts">
      <li class="contacts__item">
        <svg class="contacts__icon" viewBox="0 0 28 28" aria-hidden="true">
          <circle cx="14" cy="14" r="14" fill="var(--pink)"/>
          <path d="M10 8.5c.6-.4 1.3-.3 1.7.3l1.2 1.8c.3.5.2 1.1-.2 1.5l-.8.7c.6 1.3 1.6 2.4 2.9 3l.7-.8c.4-.4 1-.5 1.5-.2l1.8 1.2c.6.4.7 1.1.3 1.7l-.8 1c-.6.7-1.6.9-2.5.5-3-1.4-5.3-3.7-6.6-6.7-.4-.9-.1-1.9.6-2.5z" fill="#fff"/>
        </svg>
        <span>(00) 0000-0000</span>
      </li>
      <li class="contacts__item">
        <svg class="contacts__icon" viewBox="0 0 28 28" aria-hidden="true">
          <circle cx="14" cy="14" r="14" fill="var(--pink)"/>
          <rect x="7.5" y="9.5" width="13" height="9" rx="1.2" fill="none" stroke="#fff" stroke-width="1.6"/>
          <path d="M8 10.5l6 4.5 6-4.5" fill="none" stroke="#fff" stroke-width="1.6"/>
        </svg>
        <span>contato@exemplo.com</span>
      </li>
      <li class="contacts__item">
        <svg class="contacts__icon" viewBox="0 0 28 28" aria-hidden="true">
          <circle cx="14" cy="14" r="14" fill="var(--pink)"/>
          <circle cx="14" cy="14" r="6.5" fill="none" stroke="#fff" stroke-width="1.5"/>
          <ellipse cx="14" cy="14" rx="2.8" ry="6.5" fill="none" stroke="#fff" stroke-width="1.3"/>
          <path d="M7.5 14h13" stroke="#fff" stroke-width="1.3"/>
        </svg>
        <span>www.exemplo.com.br</span>
      </li>
      <li class="contacts__item">
        <svg class="contacts__icon" viewBox="0 0 28 28" aria-hidden="true">
          <circle cx="14" cy="14" r="14" fill="var(--pink)"/>
          <path d="M14 21s-5-5.2-5-9a5 5 0 0 1 10 0c0 3.8-5 9-5 9z" fill="#fff"/>
          <circle cx="14" cy="12" r="1.8" fill="var(--pink)"/>
        </svg>
        <span>rua exemplo, sl 000<br>cidade-UF, CEP: 00000-000</span>
      </li>
    </ul>

    <div class="brand brand--front">
      <span class="brand__mark" aria-hidden="true"></span>
      <span class="brand__name">Tavessa</span>
      <span class="brand__tagline">Depil e Unhas</span>
    </div>

    <svg class="card__edge" viewBox="0 0 880 30" preserveAspectRatio="none" aria-hidden="true">
      <rect x="0" y="20" width="880" height="10" fill="var(--pink)"/>
      <polygon points="0,6 130,6 150,20 0,20" fill="var(--pink)"/>
      <polygon points="880,6 750,6 730,20 880,20" fill="var(--pink)"/>
    </svg>
  </section>

  <section class="card card--back" aria-label="Verso do cartão">
    <div class="brand brand--back">
      <span class="brand__mark" aria-hidden="true"></span>
      <span class="brand__name">Tavessa</span>
      <span class="brand__tagline">Depil e Unhas</span>
    </div>

    <svg class="card__edge" viewBox="0 0 880 30" preserveAspectRatio="none" aria-hidden="true">
      <rect x="0" y="24" width="880" height="6" fill="var(--pink)"/>
      <polygon points="0,8 140,8 160,24 0,24" fill="var(--pink-deep)"/>
      <polygon points="880,8 740,8 720,24 880,24" fill="var(--pink-deep)"/>
    </svg>
  </section>

</main>
</body>
</html>
```